Marlow Law Stationery - Letterhead, Envelopes, Business Cards

We need high quality business stationery for our Personal Injury Law Firm located in Houston, Texas. The design should include the logo, Marlow Law Group, PLLC, 713-555-4718, 2150 Fernbrook Avenue, Suite 310, Houston, Texas 77019 www.MarlowLaw.example. The colors are blue and white. The letterhead should also include the Attorneys - Tessa Quill, Mitchell R. Marlow and Derek Hale.

```html
<!DOCTYPE html>
<html lang="en">
<head>
<meta charset="utf-8">
<title>Marlow Law Stationery</title>
<link rel="stylesheet" href="https://fonts.googleapis.com/css2?family=Arimo:wght@400;700&family=Open+Sans:wght@400;600&display=swap">
<style>
  :root {
    --navy: #0c1a3a;
    --paper: #ffffff;
    --card-grey: #eef0f2;
    --backdrop: #202427;
    --label: #ffffff;
    --muted: #6b6f78;
    --body: "Arimo", Arial, sans-serif;
    --label-font: "Open Sans", Arial, sans-serif;
  }
  * { box-sizing: border-box; margin: 0; padding: 0; }
  html, body { width: 1006px; height: 1200px; overflow: hidden; }
  body { background: var(--backdrop); font-family: var(--body); position: relative; }

  .section-label { position: absolute; color: var(--label); font-family: var(--label-font); font-size: 18px; font-weight: 400; }
  .section-label.is-bold { font-weight: 600; }

  .sheet { position: absolute; background: var(--paper); overflow: hidden; }

  .mark { display: flex; align-items: center; gap: 5px; color: var(--navy); font-family: var(--body); font-weight: 700; white-space: nowrap; }
  .mark-dot { border-radius: 50%; background: currentColor; flex: none; }
  .mark.on-dark { color: var(--paper); }

  .address-band { position: absolute; left: 0; right: 0; background: var(--navy); color: var(--paper); display: flex; align-items: center; gap: 4px; font-size: 7px; }
  .address-band.centered { justify-content: center; }
  .icon { width: 7px; height: 7px; fill: currentColor; flex: none; }

  .contact-line { position: absolute; left: 0; right: 0; display: flex; justify-content: center; align-items: center; gap: 3px; color: var(--muted); font-size: 6.5px; }
  .contact-line .icon { fill: var(--navy); }

  /* Business cards */
  .card { position: absolute; width: 260px; height: 149px; box-shadow: 0 6px 14px rgba(0,0,0,.45); overflow: hidden; }
  .card-front { left: 40px; top: 90px; background: var(--navy); display: flex; align-items: center; justify-content: center; }
  .card-back { left: 250px; top: 290px; background: var(--card-grey); }
  .card-back .mark { position: absolute; left: 18px; top: 44px; font-size: 11px; }
  .card-divider { position: absolute; left: 108px; top: 18px; width: 1px; height: 72px; background: #c9ccd2; }
  .card-details { position: absolute; left: 122px; top: 26px; }
  .card-name { color: var(--navy); font-weight: 700; font-size: 10px; letter-spacing: .3px; }
  .card-title { color: var(--muted); font-size: 7px; margin-bottom: 10px; }
  .card-detail { display: flex; align-items: center; gap: 4px; color: var(--muted); font-size: 7px; margin-top: 3px; }
  .card-detail .icon { fill: var(--navy); }
  .card-back .address-band { top: 104px; height: 18px; padding-left: 40px; font-size: 7px; }

  /* Note pad */
  .notepad { left: 578px; top: 169px; width: 331px; height: 233px; }
  .notepad .mark { position: absolute; left: 0; right: 0; top: 30px; justify-content: center; font-size: 13px; }
  .notepad-lines { position: absolute; left: 12px; right: 12px; top: 75px; }
  .notepad-lines span { display: block; height: 15px; border-bottom: 1px solid #8a8e96; }
  .notepad .contact-line { top: 188px; }
  .notepad .address-band { top: 202px; height: 17px; }

  /* Letterhead */
  .letterhead { left: 578px; top: 568px; width: 398px; height: 514px; }
  .letterhead .mark { position: absolute; left: 0; right: 0; top: 24px; justify-content: center; font-size: 15px; }
  .letterhead .contact-line { top: 438px; font-size: 7.5px; }
  .letterhead .address-band { top: 454px; height: 20px; font-size: 7.5px; }
  .attorneys { position: absolute; left: 0; right: 0; top: 484px; display: flex; justify-content: center; gap: 12px; }
  .attorney { text-align: center; }
  .attorney-name { color: var(--navy); font-weight: 700; font-size: 8.5px; }
  .attorney-role { color: var(--muted); font-size: 7px; }

  /* Envelopes */
  .env-front { left: 55px; top: 636px; width: 408px; height: 177px; }
  .env-front .mark { position: absolute; left: 13px; top: 98px; font-size: 13px; }
  .env-front .address-band { top: 144px; height: 19px; padding-left: 13px; font-size: 7px; }
  .env-back { left: 55px; top: 905px; width: 407px; height: 177px; }
  .env-flap { position: absolute; left: 0; top: 0; width: 407px; height: 70px; }
  .env-back .mark { position: absolute; left: 0; right: 0; top: 32px; justify-content: center; font-size: 11px; }
</style>
</head>
<body>
<svg width="0" height="0" style="position:absolute" aria-hidden="true">
  <symbol id="i-pin" viewBox="0 0 10 10"><path d="M5 0a3.6 3.6 0 0 0-3.6 3.6C1.4 6.3 5 10 5 10s3.6-3.7 3.6-6.4A3.6 3.6 0 0 0 5 0zm0 5a1.4 1.4 0 1 1 0-2.8A1.4 1.4 0 0 1 5 5z"/></symbol>
  <symbol id="i-phone" viewBox="0 0 10 10"><path d="M2.2 0.5l1.6 1.9-.9 1.3c.6 1.3 1.6 2.3 2.9 2.9l1.3-.9 1.9 1.6-.9 1.9C4.5 9.1.9 5.5.3 1.4z"/></symbol>
  <symbol id="i-globe" viewBox="0 0 10 10"><path d="M5 0a5 5 0 1 0 0 10A5 5 0 0 0 5 0zm3.9 4.4H7.2a7.6 7.6 0 0 0-.8-3.2 4 4 0 0 1 2.5 3.2zM5 1c.6.7 1.1 2 1.2 3.4H3.8C3.9 3 4.4 1.7 5 1zM3.6 1.2a7.6 7.6 0 0 0-.8 3.2H1.1a4 4 0 0 1 2.5-3.2zM1.1 5.6h1.7c.1 1.2.4 2.3.8 3.2a4 4 0 0 1-2.5-3.2zM5 9c-.6-.7-1.1-2-1.2-3.4h2.4C6.1 7 5.6 8.3 5 9zm1.4-.2c.4-.9.7-2 .8-3.2h1.7a4 4 0 0 1-2.5 3.2z"/></symbol>
</svg>

<h2 class="section-label is-bold" style="left:81px;top:40px;">Business Card_2</h2>
<div class="card card-front">
  <div class="mark on-dark" style="font-size:20px;gap:8px;"><span class="mark-dot" style="width:14px;height:14px;"></span>Marlow Law</div>
</div>
<div class="card card-back">
  <div class="mark"><span class="mark-dot" style="width:8px;height:8px;"></span>Marlow Law</div>
  <div class="card-divider"></div>
  <div class="card-details">
    <p class="card-name">TESSA QUILL</p>
    <p class="card-title">Managing Partner</p>
    <p class="card-detail"><svg class="icon"><use href="#i-phone"/></svg>713-555-4718</p>
    <p class="card-detail"><svg class="icon"><use href="#i-globe"/></svg>www.MarlowLaw.example</p>
  </div>
  <div class="address-band"><svg class="icon"><use href="#i-pin"/></svg>2150 Fernbrook Avenue, Suite 310, Houston, Texas 77019</div>
</div>

<h2 class="section-label" style="left:578px;top:134px;">Note Pads_2</h2>
<div class="sheet notepad">
  <div class="mark"><span class="mark-dot" style="width:9px;height:9px;"></span>Marlow Law</div>
  <div class="notepad-lines"><span></span><span></span><span></span><span></span><span></span><span></span><span></span></div>
  <div class="contact-line"><svg class="icon"><use href="#i-phone"/></svg>713-555-4718 | <svg class="icon"><use href="#i-globe"/></svg>www.MarlowLaw.example</div>
  <div class="address-band centered"><svg class="icon"><use href="#i-pin"/></svg>2150 Fernbrook Avenue, Suite 310, Houston, Texas 77019</div>
</div>

<h2 class="section-label" style="left:578px;top:529px;">Letterhead_2</h2>
<div class="sheet letterhead">
  <div class="mark"><span class="mark-dot" style="width:10px;height:10px;"></span>Marlow Law</div>
  <div class="contact-line"><svg class="icon"><use href="#i-phone"/></svg>713-555-4718 | <svg class="icon"><use href="#i-globe"/></svg>www.MarlowLaw.example</div>
  <div class="address-band centered"><svg class="icon"><use href="#i-pin"/></svg>2150 Fernbrook Avenue, Suite 310, Houston, Texas 77019</div>
  <div class="attorneys">
    <div class="attorney"><p class="attorney-name">MITCHELL R. MARLOW</p><p class="attorney-role">Founding partner / Attorney</p></div>
    <div class="attorney"><p class="attorney-name">TESSA QUILL</p><p class="attorney-role">Managing Partner / Associate Attorney</p></div>
    <div class="attorney"><p class="attorney-name">DEREK HALE</p><p class="attorney-role">Associate Attorney</p></div>
  </div>
</div>

<h2 class="section-label" style="left:55px;top:596px;">ENV Front_2</h2>
<div class="sheet env-front">
  <div class="mark"><span class="mark-dot" style="width:9px;height:9px;"></span>Marlow Law</div>
  <div class="address-band"><svg class="icon"><use href="#i-pin"/></svg>2150 Fernbrook Avenue, Suite 310, Houston, Texas 77019</div>
</div>

<h2 class="section-label" style="left:55px;top:865px;">ENV Back_2</h2>
<div class="sheet env-back">
  <svg class="env-flap" viewBox="0 0 407 70" aria-hidden="true">
    <path d="M1 0 C10 20 16 33 36 36 L190 63 Q203.5 66 217 63 L371 36 C391 33 397 20 406 0" fill="none" stroke="var(--navy)" stroke-width="1"/>
  </svg>
  <div class="mark"><span class="mark-dot" style="width:7px;height:7px;"></span>Marlow Law</div>
</div>
</body>
</html>
```